Gale Sentry - WEBSITE Contest - 4-5 pages coding - Strong, simple clean WORDPRESS

Hello,
The inspiriation website is www.plumeguard-sample.com
Please look at this site because I want to copy that.
I have changed the order a little bit so please look at my order of the site elements.
I will supply text, please just use lorem ipsum for now.
PLEASE LOOK AT THE PLUME GUARD WEBSITE AND MAKE A COPY OF THAT.
PPlease look at that site and see the different features it has and make that.
We will need this main page and then:
-About Us page
-Contact Us page
-Request a quote page / fillable form
-1 product/service page
Thank you,
Dorian
/////////////////////////////
Website design for Gale Sentry.
Please design with simple, easy to read fonts. Customers are older and need strong, bold easy to read.
galesentry-demo.com
Tel (555) 318-4072
dorian@galesentry-demo.com
The problem is that all roofing vents leak. We have a product that goes into the vent that stops the roof from leaking.
Your beautiful Florida home is unprotected!
All roof vents leak!
Winds over 30 MPH push rainwater INTO your home through the rooftop vents! The result is water damage that can cost thousands of dollars to repair and remediate!
The GALE SENTRY is a powerful roof vent protection system, engineered to block wind driven rains from entering your home's roof vents.
The Gale Sentry is made to withstand extreme conditions. Featuring IMPACT hurricane screening and powerful steel construction.
Professional installation is permanent and concealed and is accomplished via the roof top.
Get protected for all the storms ahead! Get the Gale Sentry!
www.galesentry-demo.com
Call Now: 555 318-4072
Updates
Hello to all designers - please add a "SERVICE AREA MAP" widget to the designs. Thank you.
Target Market(s)
The target customer is a affluent, older couple 50-60 years old. Homeowner. middle class to upper class adults / ages 50-60 years old (older but not VERY old)
Industry/Entity Type
roofing and construction
Coding
Coded - Design and coding required
Number of Pages Required
4 page
Colors
Designer to choose colors to be used in the design.
Requirements
Must have
- Great landing page, about us page, product page, contact us page, request quote form / Strong, simple clean
Nice to have
- feelings: professional / strong / reliable / safety / shelter / security / future stability/ calm / security
Should not have
- stress / fear feeling - this product will remove fear and stress of damages from storms

```html
<!DOCTYPE html>
<html lang="en">
<head>
<meta charset="utf-8">
<title>Gale Sentry – Roof Vent Protection</title>
<link href="https://fonts.googleapis.com/css2?family=Roboto:wght@400;500;700;900&display=swap" rel="stylesheet">
<style>
:root{
  --blue:#0b5e9c;
  --blue-dark:#0a4f86;
  --cyan:#1aa5c6;
  --accent:#1a8fc1;
  --ink:#333333;
  --body:#555555;
  --card:#f2f2f2;
  --footer:#2c2c2c;
  --footer-bar:#222222;
  --white:#ffffff;
}
*{margin:0;padding:0;box-sizing:border-box}
html,body{width:1200px;height:3991px;overflow:hidden;background:var(--white)}
body{font-family:'Roboto',Arial,sans-serif;color:var(--body)}
.page{position:relative;width:1200px;height:3991px;overflow:hidden}
.abs{position:absolute}
.bg-shapes{position:absolute;left:0;top:0;width:1200px;height:3991px}

/* header */
.site-header{left:0;top:0;width:1200px;height:120px;background:var(--white);z-index:3}
.brand{display:flex;align-items:center;gap:14px}
.brand-dot{width:56px;height:56px;border-radius:50%;background:var(--blue)}
.brand-name{font-size:33px;font-weight:500;color:var(--blue);letter-spacing:1px}
.header-brand{left:75px;top:32px}
.call{right:72px;top:24px;display:flex;align-items:center;gap:10px;font-size:20px;font-weight:500;color:var(--blue)}
.call-icon{width:34px;height:34px;border-radius:50%;background:var(--blue);display:flex;align-items:center;justify-content:center}
.nav{right:72px;top:82px;display:flex;gap:40px;font-size:14.5px;font-weight:700;color:var(--ink)}
.nav .active{color:var(--accent);display:flex;align-items:center;gap:6px}
.nav .active i{width:16px;height:16px;border-radius:50%;border:3px solid var(--blue);display:inline-block}

/* hero */
.hero-photo{left:0;top:120px;width:1200px;height:740px;background:linear-gradient(120deg,#6d7466 0%,#9c9f9b 35%,#c9cbc9 55%,#8d8f8c 80%,#55594f 100%)}
.hero-title{left:70px;top:305px;font-size:92px;font-weight:900;line-height:82px;color:var(--white);letter-spacing:1px}
.hero-sub{left:75px;top:488px;font-size:29px;font-weight:700;line-height:42px;color:var(--white)}
.btn{display:flex;align-items:center;justify-content:center;height:62px;border-radius:31px;background:linear-gradient(90deg,var(--blue) 0%,var(--cyan) 100%);color:var(--white);font-size:18px;font-weight:700}
.hero-btn{left:76px;top:598px;width:220px}
.hero-arrows{left:1095px;top:410px}
.hero-badge{left:726px;top:812px;width:100px;height:100px;border-radius:50%;background:var(--blue);border:8px solid var(--white);box-shadow:0 2px 6px rgba(0,0,0,.15);z-index:2}

/* welcome */
.welcome-art{left:75px;top:965px;width:510px;height:505px;border-radius:50%;background:radial-gradient(circle at 50% 50%,#2e7fa0 0%,#0d4f86 55%,#0a3a6b 100%)}
.section-title{font-size:43px;font-weight:700;line-height:47px;color:var(--ink)}
.section-title span{color:var(--blue);display:block}
.welcome-title{left:616px;top:988px}
.welcome-text{left:616px;top:1098px;width:505px;font-size:16.5px;line-height:26px}
.welcome-text p{margin-bottom:7px}
.welcome-btn{left:616px;top:1382px;width:220px}

/* services */
.services-title{left:76px;top:1678px;font-size:43px;font-weight:700;color:var(--white)}
.services-list{left:76px;top:1750px;width:505px;list-style:none;color:var(--white);font-size:16.5px;line-height:26px}
.services-list li{display:flex;gap:15px;margin-bottom:11px}
.services-list svg{flex:none;margin-top:5px}
.btn-outline{background:transparent;border:2px solid var(--white)}
.services-btn{left:74px;top:2078px;width:222px}
.services-photo{left:616px;top:1634px;width:510px;height:610px;background:linear-gradient(160deg,#6c6f70 0%,#8a8b8b 30%,#7c3a42 60%,#4a3a36 100%);box-shadow:0 4px 10px rgba(0,0,0,.2)}

/* testimonials */
.testi-title{left:0;top:2316px;width:1200px;text-align:center;font-size:43px;font-weight:700;line-height:47px;color:var(--ink)}
.testi-title span{color:var(--blue);display:block}
.card{top:2447px;width:511px;height:284px;background:var(--card);border-radius:10px;text-align:center}
.card-quote{position:absolute;left:22px;top:8px;font-size:170px;font-weight:900;line-height:170px;color:#dedede;font-family:Georgia,serif}
.card-text{position:relative;margin:52px 28px 0;font-size:16.5px;line-height:26px;color:var(--body)}
.card-name{position:relative;margin-top:16px;font-size:17px;font-weight:700;color:var(--blue)}
.card-loc{position:relative;font-size:16px;color:var(--body)}
.avatar{position:absolute;left:205px;top:243px;width:102px;height:102px;border-radius:50%;border:4px solid var(--white);background:linear-gradient(160deg,#d9b49a,#7b5a45)}
.testi-arrow{top:2588px}

/* contact */
.contact-photo{left:75px;top:2862px;width:510px;height:610px;background:linear-gradient(180deg,#dfe3e4 0%,#c8cfcf 40%,#5f6d52 70%,#8d8e88 100%);box-shadow:0 4px 10px rgba(0,0,0,.2)}
.contact-title{left:616px;top:2968px;font-size:43px;font-weight:700;color:var(--white)}
.contact-text{left:616px;top:3036px;width:510px;font-size:16.5px;line-height:26px;color:var(--white)}
.field{background:var(--white);border-radius:30px;height:60px;font-size:15px;color:var(--ink);padding:21px 20px}
.f-name{left:616px;top:3110px;width:248px}
.f-email{left:877px;top:3110px;width:249px}
.f-phone{left:616px;top:3185px;width:248px}
.f-subject{left:877px;top:3185px;width:249px}
.f-message{left:616px;top:3258px;width:510px;height:116px;border-radius:14px;padding:16px 20px}
.submit-btn{left:614px;top:3398px;width:222px}

/* footer */
.footer-brand{left:75px;top:3668px}
.footer-brand .brand-dot{background:#9a9a9a;width:62px;height:62px}
.footer-brand .brand-name{color:#cfcfcf;font-weight:400;font-size:34px}
.footer-about{left:75px;top:3765px;width:300px;font-size:14.5px;line-height:27px;color:#e5e5e5}
.foot-col h4{font-size:20px;font-weight:700;color:var(--cyan);margin-bottom:14px}
.foot-col li{list-style:none;font-size:14.5px;line-height:32.5px;color:#e5e5e5}
.col-links{left:434px;top:3668px}
.col-services{left:643px;top:3668px}
.col-contact{left:884px;top:3668px;width:240px}
.col-contact li{display:flex;gap:16px;line-height:26px;margin-bottom:11px}
.col-contact svg{flex:none;margin-top:6px}
.socials{left:884px;top:3860px;display:flex;gap:20px}
.socials i{width:20px;height:20px;background:#ececec;border-radius:3px;display:block}
.footer-bar{left:0;top:3925px;width:1200px;height:66px;background:var(--footer-bar);color:#e5e5e5;font-size:14.5px;text-align:center;padding-top:32px}
</style>
</head>
<body>
<div class="page">

  <svg class="bg-shapes" viewBox="0 0 1200 3991" aria-hidden="true">
    <defs>
      <linearGradient id="band" x1="0" y1="0" x2="0" y2="1">
        <stop offset="0" stop-color="#1aa5c6"/>
        <stop offset="1" stop-color="#0b5b98"/>
      </linearGradient>
    </defs>
    <path d="M0 1635 C400 1545 800 1590 1200 1485 L1200 2130 C800 2195 400 2215 0 2250 Z" fill="url(#band)"/>
    <path d="M0 2975 C300 2920 700 2905 1200 2855 L1200 3620 L0 3620 Z" fill="url(#band)"/>
    <path d="M0 3560 C400 3640 800 3640 1200 3520 L1200 3991 L0 3991 Z" fill="#2c2c2c"/>
  </svg>

  <!-- Header -->
  <header class="abs site-header">
    <div class="abs brand header-brand"><span class="brand-dot"></span><span class="brand-name">GALE SENTRY</span></div>
    <div class="abs call">
      <span class="call-icon"><svg width="18" height="18" viewBox="0 0 24 24"><path fill="#fff" d="M6.6 10.8a15.1 15.1 0 0 0 6.6 6.6l2.2-2.2a1 1 0 0 1 1-.25 11.4 11.4 0 0 0 3.6.57 1 1 0 0 1 1 1V20a1 1 0 0 1-1 1A17 17 0 0 1 3 4a1 1 0 0 1 1-1h3.5a1 1 0 0 1 1 1c0 1.25.2 2.45.57 3.57a1 1 0 0 1-.25 1z"/></svg></span>
      Call Now: 555 318-4072
    </div>
    <nav class="abs nav">
      <span class="active"><i></i>HOME</span><span>ABOUT US</span><span>SERVICES</span><span>TESTIMONIALS</span><span>BLOG</span><span>CONTACT US</span>
    </nav>
  </header>

  <!-- Hero -->
  <div class="abs hero-photo" role="img" aria-label="Photo of a steel roof vent protector installed on a rooftop"></div>
  <svg class="abs" style="left:0;top:770px" width="1200" height="95" viewBox="0 0 1200 95" aria-hidden="true"><path d="M0 13 C350 60 700 95 1200 10 L1200 95 L0 95 Z" fill="#fff"/></svg>
  <h1 class="abs hero-title">GALE<br>SENTRY</h1>
  <p class="abs hero-sub">Your beautiful Florida home is unprotected!<br>All roof vents leak!</p>
  <a class="abs btn hero-btn">READ MORE</a>
  <svg class="abs hero-arrows" width="50" height="145" viewBox="0 0 50 145" aria-hidden="true">
    <polyline points="8,6 42,36 8,66" fill="none" stroke="#fff" stroke-width="4"/>
    <polyline points="42,76 8,106 42,136" fill="none" stroke="#fff" stroke-width="4"/>
  </svg>
  <div class="abs hero-badge"></div>

  <!-- Welcome -->
  <div class="abs welcome-art" role="img" aria-label="Circular photo of palm trees bending in a storm"></div>
  <h2 class="abs section-title welcome-title">WELCOME TO<span>GALE SENTRY</span></h2>
  <div class="abs welcome-text">
    <p>Sed ut perspiciatis unde omnis iste natus error sit voluptatem accusantium doloremque laudantium, totam rem aperiam, eaque ipsa quae ab illo inventore veritatis et quasi architecto beatae vitae dicta sunt explicabo.</p>
    <p>Nemo enim ipsam voluptatem quia voluptas sit aspernatur aut odit aut fugit, sed quia consequuntur magni dolores eos qui ratione voluptatem sequi nesciunt.</p>
    <p>Nam libero tempore, cum soluta nobis est eligendi optio cumque nihil impedit quo minus id quod maxime.</p>
  </div>
  <a class="abs btn welcome-btn">READ MORE</a>

  <!-- Services -->
  <h2 class="abs services-title">OUR SERVICES</h2>
  <ul class="abs services-list">
    <li><svg width="16" height="16" viewBox="0 0 16 16"><circle cx="8" cy="8" r="6.5" fill="none" stroke="#fff" stroke-width="1.5"/><polyline points="4.8,8.2 7,10.3 11.2,5.8" fill="none" stroke="#fff" stroke-width="1.5"/></svg><span>The GALE SENTRY is a powerful roof vent protection system, engineered to block wind driven rains from entering your home's roof vents.</span></li>
    <li><svg width="16" height="16" viewBox="0 0 16 16"><circle cx="8" cy="8" r="6.5" fill="none" stroke="#fff" stroke-width="1.5"/><polyline points="4.8,8.2 7,10.3 11.2,5.8" fill="none" stroke="#fff" stroke-width="1.5"/></svg><span>The Gale Sentry is made to withstand extreme conditions. Featuring IMPACT hurricane screening and powerful steel construction.</span></li>
    <li><svg width="16" height="16" viewBox="0 0 16 16"><circle cx="8" cy="8" r="6.5" fill="none" stroke="#fff" stroke-width="1.5"/><polyline points="4.8,8.2 7,10.3 11.2,5.8" fill="none" stroke="#fff" stroke-width="1.5"/></svg><span>Professional installation is permanent and concealed and is accomplished via the roof top.</span></li>
    <li><svg width="16" height="16" viewBox="0 0 16 16"><circle cx="8" cy="8" r="6.5" fill="none" stroke="#fff" stroke-width="1.5"/><polyline points="4.8,8.2 7,10.3 11.2,5.8" fill="none" stroke="#fff" stroke-width="1.5"/></svg><span>Get protected for all the storms ahead!<br>Get the Gale Sentry!</span></li>
  </ul>
  <a class="abs btn btn-outline services-btn">READ MORE</a>
  <div class="abs services-photo" role="img" aria-label="Photo of a red tiled roof in heavy wind-driven rain"></div>

  <!-- Testimonials -->
  <h2 class="abs testi-title">WHAT OUR<span>CUSTOMERS SAYING</span></h2>
  <div class="abs card" style="left:75px">
    <div class="card-quote">“</div>
    <p class="card-text">" Sed ut perspiciatis unde omnis iste natus error sit voluptatem accusantium doloremque laudantium, totam rem aperiam, eaque ipsa quae ab illo inventore veritatis et quasi architecto beatae vitae dicta sunt explicabo.</p>
    <p class="card-name">NAME HEADING</p>
    <p class="card-loc">Location</p>
    <div class="avatar" role="img" aria-label="Customer portrait photo"></div>
  </div>
  <div class="abs card" style="left:616px">
    <div class="card-quote">“</div>
    <p class="card-text">" Sed ut perspiciatis unde omnis iste natus error sit voluptatem accusantium doloremque laudantium, totam rem aperiam, eaque ipsa quae ab illo inventore veritatis et quasi architecto beatae vitae dicta sunt explicabo.</p>
    <p class="card-name">NAME HEADING</p>
    <p class="card-loc">Location</p>
    <div class="avatar" role="img" aria-label="Customer portrait photo" style="background:linear-gradient(160deg,#c49a7c,#4d6a7a)"></div>
  </div>
  <svg class="abs testi-arrow" style="left:32px" width="28" height="50" viewBox="0 0 28 50" aria-hidden="true"><polyline points="24,3 4,25 24,47" fill="none" stroke="#aaa" stroke-width="2.5"/></svg>
  <svg class="abs testi-arrow" style="left:1140px" width="28" height="50" viewBox="0 0 28 50" aria-hidden="true"><polyline points="4,3 24,25 4,47" fill="none" stroke="#aaa" stroke-width="2.5"/></svg>

  <!-- Contact -->
  <div class="abs contact-photo" role="img" aria-label="Photo of palm trees bending over a house during a hurricane"></div>
  <h2 class="abs contact-title">QUICK CONTACT</h2>
  <p class="abs contact-text">Nemo enim ipsam voluptatem quia voluptas sit aspernatur aut odit aut fugit, sed quia consequuntur magni dolores.</p>
  <div class="abs field f-name">Name</div>
  <div class="abs field f-email">Email Address</div>
  <div class="abs field f-phone">Phone No</div>
  <div class="abs field f-subject">Subject</div>
  <div class="abs field f-message">Message</div>
  <a class="abs btn btn-outline submit-btn">SUBMIT</a>

  <!-- Footer -->
  <div class="abs brand footer-brand"><span class="brand-dot"></span><span class="brand-name">GALE SENTRY</span></div>
  <p class="abs footer-about">Excepteur sint occaecat cupidatat non proident, sunt in culpa qui officia deserunt mollit anim id est laborum.</p>
  <div class="abs foot-col col-links"><h4>QUICK LINKS</h4><ul><li>Home</li><li>About Us</li><li>Services</li><li>Testimonials</li><li>Blog</li><li>Contact Us</li></ul></div>
  <div class="abs foot-col col-services"><h4>SERVICES</h4><ul><li>Excepteur sint occaecat</li><li>Cupidatat non</li><li>Proident suntn culpa</li><li>Qui officia deserunt</li><li>Mollit anim</li></ul></div>
  <div class="abs foot-col col-contact"><h4>CONTACT US</h4><ul>
    <li><svg width="16" height="14" viewBox="0 0 16 14"><path d="M1 2 L5 1 L11 3 L15 2 L15 12 L11 13 L5 11 L1 12 Z" fill="#1aa5c6"/></svg><span>Excepteur sint occaecatcup at non proidentsunt</span></li>
    <li><svg width="16" height="14" viewBox="0 0 24 24"><path fill="#1aa5c6" d="M6.6 10.8a15.1 15.1 0 0 0 6.6 6.6l2.2-2.2a1 1 0 0 1 1-.25 11.4 11.4 0 0 0 3.6.57 1 1 0 0 1 1 1V20a1 1 0 0 1-1 1A17 17 0 0 1 3 4a1 1 0 0 1 1-1h3.5a1 1 0 0 1 1 1c0 1.25.2 2.45.57 3.57a1 1 0 0 1-.25 1z"/></svg><span>555 318-4072</span></li>
    <li><svg width="16" height="14" viewBox="0 0 16 14"><rect x="1" y="2" width="14" height="10" fill="#1aa5c6"/><polyline points="1,2 8,8 15,2" fill="none" stroke="#2c2c2c" stroke-width="1.3"/></svg><span>info@companyname,com</span></li>
  </ul></div>
  <div class="abs socials"><i></i><i></i><i></i><i></i></div>
  <div class="abs footer-bar">©2022 by Company Name. All Right Reserved</div>

</div>
</body>
</html>
```